Hot sauce company needs a logo and label design- simple, clean & fresh

Toby K's a hot pepper sauce company based on the edge of London needs a logo and label design .
The sauces are handmade in small batches with natural ingredients , no added sugars or extracts and so we would like a clean fresh label to reflect this - avoiding all the macho devil and flames novelty stuff.
At present there are four sauces - Jalapeno ,Chipotle,Habanero and Reaper we would like to have one Toby K's label with the name of the sauce being changeable allowing us to react to what ingredients are available .
Updates

Project Deadline Extended
Reason: Hi Guys I have received a few requests to extend the deadline on the project and so I am thanks Toby K's

Target Market(s)

people who care what they eat

Industry/Entity Type

Food Store

Logo Text

Toby K's handmade hot sauce

Requirements
Must have
• Toby K's handmade hot sauce - or the logo
• the name of the sauce ie jalapeno
• no added sugars
Nice to have
• handmade
• small batch
Should not have
• cartoon men with smoke coming out of their ears
• devils and the flames of hell

```html
<!DOCTYPE html>
<html lang="en">
<head>
<meta charset="utf-8">
<title>Toby K's – Logo and Labels</title>
<link rel="stylesheet" href="https://fonts.googleapis.com/css2?family=Open+Sans:wght@400;600;800&display=swap">
<style>
  :root {
    --brown: #6b3b3c;
    --cream: #f2ece4;
    --white: #ffffff;
    --jalapeno: #3a9a0c;
    --habanero: #f57b1f;
  }
  * { margin: 0; padding: 0; box-sizing: border-box; }
  html, body { width: 1200px; height: 746px; overflow: hidden; background: var(--white); }
  .canvas { position: relative; width: 1200px; height: 746px; }

  .brand {
    position: absolute;
    left: 0; right: 0;
    text-align: center;
    color: var(--brown);
    font-family: "Open Sans", sans-serif;
    white-space: nowrap;
  }
  .brand__name { font-weight: 600; line-height: 1; }
  .brand__tagline { font-weight: 400; text-transform: uppercase; line-height: 1; }

  .brand--main { top: 88px; }
  .brand--main .brand__name { font-size: 80px; }
  .brand--main .brand__tagline { margin-top: 18px; font-size: 24px; letter-spacing: 4px; }

  .label {
    position: absolute;
    top: 281px;
    width: 390px;
    height: 389px;
    background: var(--cream);
  }
  .label--jalapeno { left: 192px; --accent: var(--jalapeno); }
  .label--habanero { left: 618px; --accent: var(--habanero); }

  .label__frame {
    position: absolute;
    left: 14px; top: 11px; right: 10px; bottom: 10px;
    border: 2px solid var(--accent);
  }
  .label__band {
    position: absolute;
    left: 14px; right: 10px; bottom: 10px; height: 51px;
    background: var(--accent);
  }
  .brand--label { top: 38px; }
  .brand--label .brand__name { font-size: 36px; }
  .brand--label .brand__tagline { margin-top: 8px; font-size: 11px; letter-spacing: 2px; }

  .label__art {
    position: absolute;
    top: 122px;
    height: 174px;
    border-radius: 48% 52% 45% 55% / 55% 50% 50% 45%;
    background: var(--accent);
    display: flex;
    align-items: center;
    justify-content: center;
  }
  .label--jalapeno .label__art { left: 48px; width: 292px; }
  .label--habanero .label__art { left: 38px; width: 324px; }

  .label__sauce {
    font-family: "Open Sans", sans-serif;
    font-weight: 800;
    font-size: 44px;
    line-height: 1;
    color: var(--white);
    text-transform: uppercase;
  }

  .label__claims {
    position: absolute;
    left: 50%;
    transform: translateX(-50%);
    bottom: 18px;
    width: 142px;
    padding: 6px 0 4px;
    border-radius: 8px 8px 0 0;
    background: var(--accent);
    list-style: none;
    font-family: "Open Sans", sans-serif;
    font-size: 10.5px;
    line-height: 13.6px;
    color: var(--white);
    text-align: center;
  }
</style>
</head>
<body>
<main class="canvas">
  <header class="brand brand--main">
    <h1 class="brand__name">Toby K's</h1>
    <p class="brand__tagline">Handmade hot sauce</p>
  </header>

  <section class="label label--jalapeno" aria-label="Jalapeño sauce label">
    <div class="label__frame"></div>
    <div class="label__band"></div>
    <div class="brand brand--label">
      <p class="brand__name">Toby K's</p>
      <p class="brand__tagline">Handmade hot sauce</p>
    </div>
    <div class="label__art" role="img" aria-label="Green jalapeño pepper illustration with splashes">
      <h2 class="label__sauce">Jalapeño</h2>
    </div>
    <ul class="label__claims">
      <li>natural ingredients</li>
      <li>no added sugars</li>
      <li>handmade</li>
      <li>small batch</li>
    </ul>
  </section>

  <section class="label label--habanero" aria-label="Habanero sauce label">
    <div class="label__frame"></div>
    <div class="label__band"></div>
    <div class="brand brand--label">
      <p class="brand__name">Toby K's</p>
      <p class="brand__tagline">Handmade hot sauce</p>
    </div>
    <div class="label__art" role="img" aria-label="Orange habanero pepper illustration with splashes">
      <h2 class="label__sauce">Habanero</h2>
    </div>
    <ul class="label__claims">
      <li>natural ingredients</li>
      <li>no added sugars</li>
      <li>handmade</li>
      <li>small batch</li>
    </ul>
  </section>
</main>
</body>
</html>
```